WordPress WEB DESIGN & CODING for www.quelbrix-aerial.com Wireless Tower Contruction

WEB DESIGN & CODING for www.quelbrix-aerial.com
Wireless Tower Contruction Industry

SLOGAN: SERVICE AT A HIGHER LEVEL

Brannock Spires LLC has been in business since 2014 with combined professional Team experience of over 40 years.

Our Team is composed of long-time industry professionals in every aspect of the wireless telecommunications and commercial construction industries, including project management and site acquisition.

Brannock Spires specializes in providing tower installation services for the Wireless Telecommunications in the Southeastern of the United States.

Our key services are Wireless Tower Construction, Installation & Maintenance

Site audits and Tower mapping
Mount swaps and Modifications
Hardline & Jumper Installation
Antenna & Radio Install, Decom, Testing and Maintenance
Tower Lighting Installation & Testing
Fiber / Sweep / RET/ PIM Testing
Small Cells
Civil installation (concrete/steel platforms/electrical)
____________________________________________________________________

we need a clean yet vibrant, energetic website design that will convey our tower installation work to the fullest... It should use the navy and green colors of our logo and it must be mobile friendly and coded for both Android & IOS;
the site structure:
HOME
ABOUT
SERVICES
CONTRACT
CAREERS
GALLERY

I also attach a few pics we bought on shutterstock so these can be used if needed as we own them...

Target Market(s)

Client: large companies looking for general contractor or installation contractor in the market

Industry/Entity Type

Wireless Communication

Coding

Coded - Design and coding required

Number of Pages Required

4 page

Font styles to use
Sans Serif

Colors
0555a3
00a990
ffffff

Requirements
Must have
• Wordpress - must be both desktop mobile friendly and mobile is the key -
• should open swiftly on both Android & iOS
• See power point file with presentation about the company; page 5 is our keyservices but other contents can be used too
Nice to have
• panorama pics changing from the height/tower view showing the full overview, could be a slideshow or a short video...
Should not have
• flash animation does not work on iOS so this should be avoided.

```html
<!DOCTYPE html>
<html lang="en">
<head>
<meta charset="utf-8">
<title>Brannock Spires – Wireless Tower Construction</title>
<link href="https://fonts.googleapis.com/css2?family=Roboto:wght@300;400;500;700&display=swap" rel="stylesheet">
<style>
:root{
  --navy:#0555a3;
  --green:#00a990;
  --white:#ffffff;
  --ink:#333333;
  --icon:#111111;
}
*{margin:0;padding:0;box-sizing:border-box}
html,body{width:1200px;height:5123px;overflow:hidden;background:var(--white);font-family:'Roboto',Arial,sans-serif;color:var(--ink)}
.page{position:relative;width:1200px;height:5123px}
.abs{position:absolute}

/* header */
.site-header{left:0;top:0;width:1200px;height:74px;background:var(--white);border-bottom:2px solid #d6dde6}
.brand{left:96px;top:25px;font-size:17px;font-weight:500;color:var(--navy);display:flex;align-items:center;gap:7px;white-space:nowrap}
.brand-dot{width:12px;height:12px;background:var(--green);border-radius:50%}
.nav a{position:absolute;top:32px;font-size:13px;color:#555;text-decoration:none}
.nav-cta{left:904px;top:25px;width:122px;height:28px;border-radius:14px;background:var(--navy);color:var(--white);font-size:10px;display:flex;align-items:center;justify-content:center}

/* hero */
.hero{left:0;top:74px;width:1200px;height:560px;background:linear-gradient(110deg,#6fb79a 0%,#9cc6b1 25%,#6ea0c4 55%,#2f6bb0 80%,#1a55a0 100%)}
.hero-title{left:0;top:232px;width:1200px;text-align:center;color:var(--white);font-weight:700;font-size:28px}
.hero-title .name{color:var(--navy);font-size:38px;margin-right:8px}
.hero-slogan{left:0;top:305px;width:1200px;text-align:center;color:var(--white);font-weight:300;font-size:40px}
.hero-btn{left:505px;top:390px;width:186px;height:42px;border-radius:21px;background:var(--navy);color:var(--white);font-size:16px;display:flex;align-items:center;justify-content:center}
.dots{left:576px;top:475px;display:flex;gap:8px}
.dots span{width:10px;height:10px;border-radius:50%;border:1.5px solid var(--navy)}
.dots span.on{background:var(--navy)}
.scroll{left:0;top:570px;width:1200px;text-align:center;color:var(--white);font-size:14px;letter-spacing:.5px}
.scroll-line{left:599px;top:592px;width:1px;height:42px;background:rgba(255,255,255,.8)}
.scroll-ring{left:594px;top:592px;width:12px;height:12px;border:1.5px solid #fff;border-radius:50%}

.section-title{color:var(--navy);font-weight:700;font-size:33px;text-align:center}

/* about */
.about-art{left:210px;top:920px;width:250px;height:335px;background:linear-gradient(180deg,#e6eef8,#d2e0f1);border-radius:6px}
.about-text{left:535px;top:925px;width:445px;font-size:19px;line-height:24px;color:var(--navy)}

/* services */
.svc{width:150px;height:150px;border-radius:50%;display:flex;align-items:center;justify-content:center}
.svc.green{background:var(--green)}
.svc.navy{background:var(--navy)}
.svc svg{width:78px;height:78px;fill:none;stroke:var(--icon);stroke-width:1.4;stroke-linecap:round;stroke-linejoin:round}
.svc-label{width:200px;text-align:center;font-size:19px;line-height:25px;color:#333}

/* callback */
.field{left:194px;width:376px;height:37px;border:2px solid var(--navy);font-size:19px;color:#777;padding:4px 12px}
.submit{left:255px;top:2953px;width:254px;height:59px;background:var(--navy);color:var(--white);font-weight:500;font-size:21px;display:flex;align-items:center;justify-content:center}
.agent-frame{left:662px;top:2625px;width:390px;height:377px;border:4px solid var(--navy);border-radius:100px;display:flex;align-items:center;justify-content:center}
.agent-art{width:250px;height:270px;border-radius:20px;background:linear-gradient(180deg,#d7e4f3,#b9cfe8)}

/* gallery */
.tile{position:absolute}
.see-more{left:76px;top:3866px;width:345px;height:224px;background:var(--navy);color:var(--white);font-weight:700;font-size:21px;display:flex;flex-direction:column;align-items:center;justify-content:center;gap:22px}

/* footer */
.footer{left:0;top:4272px;width:1200px;height:851px;background:linear-gradient(160deg,#1a5fae 0%,#0b4d9b 45%,#1c5ba6 75%,#0a4891 100%)}
.f-head{font-size:24px;color:var(--white);font-weight:400}
.f-text{font-size:19px;color:var(--white);line-height:45px}
.f-link{position:absolute;font-size:19px;color:var(--white);text-decoration:underline}
.f-btn{left:150px;top:4830px;width:310px;height:70px;border:2px solid #fff;border-radius:35px;color:#fff;font-size:15px;display:flex;align-items:center;justify-content:center}
.copyright{left:155px;top:5058px;font-size:19px;color:var(--white);letter-spacing:1px}
.social{top:5059px;width:24px;height:24px;border-radius:50%;background:var(--white)}
</style>
</head>
<body>
<div class="page">

  <header class="abs site-header">
    <div class="abs brand"><span class="brand-dot"></span>Brannock Spires</div>
    <nav class="nav">
      <a style="left:265px">HOME</a>
      <a style="left:357px">ABOUT</a>
      <a style="left:453px">SERVICES</a>
      <a style="left:568px">CONTRACT</a>
      <a style="left:693px">CAREERS</a>
      <a style="left:806px">GALLERY</a>
    </nav>
    <div class="abs nav-cta">CONTACT US</div>
  </header>

  <section class="abs hero" role="img" aria-label="Telecom lattice tower against a bright sky with clouds"></section>
  <h1 class="abs hero-title"><span class="name">Brannock Spires</span>Wireless Tower Construction</h1>
  <p class="abs hero-slogan">SERVICE AT A HIGHER LEVEL</p>
  <div class="abs hero-btn">CONTACT US</div>
  <div class="abs dots"><span class="on"></span><span></span><span></span></div>
  <div class="abs scroll">Scroll Down For More</div>
  <div class="abs scroll-line"></div>
  <div class="abs scroll-ring"></div>

  <h2 class="abs section-title" style="left:345px;top:822px;width:400px">ABOUT US</h2>
  <div class="abs about-art" role="img" aria-label="Line illustration of a radio tower broadcasting signals"></div>
  <p class="abs about-text">Lorem ipsum dolor sit amet, consectetur adipiscing elit. Donec auctor turpis lectus, quis scvelerisque eros fringilla sit amet. Aenean id lorem sed libero volutpat ultrices. Mauris eu fermentum orci, ut imperdiet elit. Pellentesque quis libero nisi. Ut semper nulla eget ultricies commodo. Donec blandit libero at diam rutrum, nec porttitor ex dignissim. Quisque vulputate urna velit, id dignissim neque semper vel. Nullam scelerisque tincidunt sodales. Praesent in vestibulum nibh. Cras non tortor in diam euismod aliquam vel eu erat. Phasellus scelerisque sapien eu nulla mollis tempor</p>

  <h2 class="abs section-title" style="left:300px;top:1543px;width:600px">SERVICES OFFERED</h2>

  <!-- row 1 -->
  <div class="abs svc green" style="left:176px;top:1660px">
    <svg viewBox="0 0 24 24" aria-hidden="true"><path d="M12 2L7 22M12 2l5 20M8 8h8M6 6h12M9 12h6M8.5 14l7 4M15.5 14l-7 4"/></svg>
  </div>
  <div class="abs svc navy" style="left:350px;top:1660px">
    <svg viewBox="0 0 24 24" aria-hidden="true"><circle cx="12" cy="7" r="1.5"/><path d="M8.5 4a5 5 0 000 6M15.5 4a5 5 0 010 6M6 2a8 8 0 000 10M18 2a8 8 0 010 10M12 8.5L8 21M12 8.5L16 21M9.5 15h5M5 15h5v7H5zM6.5 18h2"/></svg>
  </div>
  <div class="abs svc green" style="left:525px;top:1660px">
    <svg viewBox="0 0 24 24" aria-hidden="true"><rect x="5" y="5" width="14" height="14" rx="1.5"/><rect x="8" y="8" width="8" height="8"/><path d="M8 2v3M12 2v3M16 2v3M8 19v3M12 19v3M16 19v3M2 8h3M2 12h3M2 16h3M19 8h3M19 12h3M19 16h3"/></svg>
  </div>
  <div class="abs svc navy" style="left:700px;top:1660px">
    <svg viewBox="0 0 24 24" aria-hidden="true"><rect x="3" y="8" width="18" height="12" rx="2"/><path d="M7 8l10-4M6 11h12"/><circle cx="7" cy="16" r="1"/><circle cx="10" cy="16" r="1"/><circle cx="16" cy="15.5" r="2"/></svg>
  </div>
  <div class="abs svc green" style="left:874px;top:1660px">
    <svg viewBox="0 0 24 24" aria-hidden="true"><path d="M12 3l9 5-9 5-9-5z"/><path d="M3 12l9 5 9-5"/><path d="M3 16l9 5 9-5"/></svg>
  </div>
  <div class="abs svc-label" style="left:151px;top:1822px">Site Audits<br>&amp;<br>Tower mapping</div>
  <div class="abs svc-label" style="left:325px;top:1822px">Mount swaps<br>&amp;<br>Modifications</div>
  <div class="abs svc-label" style="left:500px;top:1822px">Hardline &amp;<br>Jumper<br>Installation</div>
  <div class="abs svc-label" style="left:675px;top:1822px">Antenna<br>&amp;<br>Radio Install,</div>
  <div class="abs svc-label" style="left:849px;top:1822px">Decom,<br>Testing &amp;<br>Maintenance</div>

  <!-- row 2 -->
  <div class="abs svc navy" style="left:176px;top:1945px">
    <svg viewBox="0 0 24 24" aria-hidden="true"><path d="M12 2v20M5 6h14M7 10h10M5 6v2M19 6v2M7 10v2M17 10v2M12 14c3 0 4 2 6 2"/></svg>
  </div>
  <div class="abs svc green" style="left:343px;top:1945px">
    <svg viewBox="0 0 24 24" aria-hidden="true"><rect x="3" y="6" width="18" height="13" rx="1"/><rect x="6" y="9" width="12" height="7"/><path d="M7 6V3h2M16 6V3h-2M2 21h20"/><circle cx="12" cy="12.5" r="1"/><path d="M10 11a3 3 0 000 3M14 11a3 3 0 010 3"/></svg>
  </div>
  <div class="abs svc navy" style="left:510px;top:1945px">
    <svg viewBox="0 0 24 24" aria-hidden="true"><circle cx="12" cy="17" r="5"/><path d="M9 3v8M12 2v9M15 3v8"/><circle cx="9" cy="3" r="1"/><circle cx="15" cy="3" r="1"/></svg>
  </div>
  <div class="abs svc green" style="left:690px;top:1945px">
    <svg viewBox="0 0 24 24" aria-hidden="true"><circle cx="12" cy="12" r="10"/><circle cx="12" cy="12" r="7"/><ellipse cx="12" cy="12" rx="3" ry="7"/><path d="M5 12h14M12 5v14"/></svg>
  </div>
  <div class="abs svc navy" style="left:874px;top:1945px">
    <svg viewBox="0 0 24 24" aria-hidden="true" style="stroke:none;fill:var(--icon)"><path d="M6.6 10.8c1.4 2.8 3.8 5.1 6.6 6.6l2.2-2.2c.3-.3.7-.4 1-.2 1.1.4 2.3.6 3.6.6.6 0 1 .4 1 1V20c0 .6-.4 1-1 1C10.6 21 3 13.4 3 4c0-.6.4-1 1-1h3.5c.6 0 1 .4 1 1 0 1.3.2 2.5.6 3.6.1.3 0 .7-.2 1L6.6 10.8z"/></svg>
  </div>
  <div class="abs svc-label" style="left:151px;top:2106px">Tower Lighting<br>Installation<br>&amp; Testing</div>
  <div class="abs svc-label" style="left:318px;top:2106px">Fiber / Sweep<br>/ RET/ PIM<br>Testing</div>
  <div class="abs svc-label" style="left:485px;top:2106px">Small<br>Cells</div>
  <div class="abs svc-label" style="left:640px;top:2103px;width:250px">Civil installation<br>(concrete/steel<br>platforms/electrical</div>
  <div class="abs svc-label" style="left:849px;top:2106px">Contact<br>Us</div>

  <h2 class="abs section-title" style="left:250px;top:2515px;width:700px">GET A CALLBACK FROM US</h2>
  <div class="abs field" style="top:2638px">Your Name:</div>
  <div class="abs field" style="top:2707px">Phone No:</div>
  <div class="abs field" style="top:2776px">Your E-mail:</div>
  <div class="abs field" style="top:2843px;height:78px">Message :</div>
  <div class="abs submit">SUBMIT</div>
  <div class="abs agent-frame"><div class="agent-art" role="img" aria-label="Support agent wearing a headset"></div></div>

  <h2 class="abs section-title" style="left:390px;top:3318px;width:400px;font-size:44px">GALLERY</h2>
  <div class="tile" style="left:76px;top:3402px;width:699px;height:223px;background:linear-gradient(180deg,#f2f2f2,#bdbdbd)" role="img" aria-label="Black and white telecom towers"></div>
  <div class="tile" style="left:780px;top:3402px;width:344px;height:223px;background:linear-gradient(180deg,#e8e8e8,#9a9a9a)" role="img" aria-label="Looking up inside a lattice tower"></div>
  <div class="tile" style="left:76px;top:3634px;width:345px;height:223px;background:linear-gradient(180deg,#d5b98d,#6a5030)" role="img" aria-label="Tower silhouette at sunset"></div>
  <div class="tile" style="left:428px;top:3634px;width:345px;height:223px;background:linear-gradient(160deg,#4c6f98,#c9d6e4 60%,#8fa6c0)" role="img" aria-label="Tower with sunburst and clouds"></div>
  <div class="tile" style="left:780px;top:3634px;width:344px;height:223px;background:linear-gradient(180deg,#2c4a9a,#1a2c55)" role="img" aria-label="Antennas mounted on a tower"></div>
  <div class="abs see-more">
    <svg width="86" height="74" viewBox="0 0 86 74" aria-hidden="true"><rect x="12" y="2" width="72" height="58" fill="none" stroke="#fff" stroke-width="4"/><path d="M2 14v58h70" fill="none" stroke="#fff" stroke-width="4"/><path d="M18 54l18-22 12 14 8-8 22 16z" fill="#fff"/><circle cx="62" cy="18" r="6" fill="#fff"/></svg>
    SEE MORE
  </div>
  <div class="tile" style="left:428px;top:3866px;width:696px;height:224px;background:linear-gradient(180deg,#c9a0b3,#e1b1a8 60%,#8a6a60)" role="img" aria-label="Rooftop antennas at dusk"></div>

  <footer class="abs footer" role="img" aria-label="Aerial city view in navy tint"></footer>
  <div class="abs f-head" style="left:152px;top:4365px">CONTACT US</div>
  <div class="abs f-head" style="left:540px;top:4365px">SITEMAP</div>
  <div class="abs f-head" style="left:892px;top:4365px">ABOUT</div>
  <div class="abs f-text" style="left:152px;top:4457px">Brannock Spires wireless ltd<br>(555-210-4836)</div>
  <div class="abs f-text" style="left:152px;top:4590px">9am - 6pm ET,<br>Monday - Friday</div>
  <div class="abs f-text" style="left:152px;top:4718px">info@quelbrix-aerial.com</div>
  <div class="abs f-btn">SCHEDULE FREE CONSULTATION</div>
  <a class="f-link" style="left:540px;top:4457px">HOME</a>
  <a class="f-link" style="left:540px;top:4525px">ABOUT</a>
  <a class="f-link" style="left:540px;top:4593px">SERVICES</a>
  <a class="f-link" style="left:540px;top:4660px">CONTRACT</a>
  <a class="f-link" style="left:540px;top:4727px">CAREERS</a>
  <a class="f-link" style="left:540px;top:4795px">GALLERY</a>
  <a class="f-link" style="left:892px;top:4470px">FAQ</a>
  <a class="f-link" style="left:892px;top:4537px">Contact Us</a>
  <a class="f-link" style="left:892px;top:4605px">Careers</a>
  <a class="f-link" style="left:892px;top:4672px">Terms of Service,</a>
  <a class="f-link" style="left:892px;top:4740px">Privacy</a>
  <div class="abs copyright">copyright 2019 @Halvorsen Digital Studio pvt ltd.</div>
  <div class="abs social" style="left:866px"></div>
  <div class="abs social" style="left:918px"></div>
  <div class="abs social" style="left:971px"></div>
  <div class="abs social" style="left:1023px"></div>

</div>
</body>
</html>
```